Professional Modern Website Design

We are a premium IT services provider to the financial industry based in London. Our company is called Veltra our current holding page is www.veltra-example.co.uk. We require a new website to match our new corporate identity. This project is for the design phase only. Development will be handled in-house. I have attached examples of wire frames we have developed (although open to suggestions for improvement) Our brand document that should demonstrate current brand, inc how we communicate to potential clients and finally mostly completed web-content.
We are looking for designers that can create something that sets us apart from our competitors.
Target Market(s)
IT Decision makers in Finance companies such as; hedge funds, private investment banks etc
Industry/Entity Type
Financial
Number of Pages Required
5+ page
Requirements
Must have
- hexagon elements in the design, unique design.
Nice to have
- Blog and social media feeds
Should not have
- Should not resemble a downloaded template

```html
<!DOCTYPE html>
<html lang="en">
<head>
<meta charset="utf-8">
<title>Veltra – Systems Integration for Finance</title>
<link rel="stylesheet" href="https://fonts.googleapis.com/css2?family=Roboto+Condensed:wght@300;400;700&display=swap">
<style>
  :root {
    --orange: #f07421;
    --orange-dark: #d85f12;
    --ink: #1c1c1c;
    --body: #333333;
    --white: #ffffff;
    --panel: #eeeeee;
    --footer: #1f1f1f;
    --footer-base: #141414;
    --muted: #6f6f6f;
    --rule: #d8d8d8;
  }
  * { margin: 0; padding: 0; box-sizing: border-box; }
  html, body { width: 1200px; height: 2550px; overflow: hidden; }
  body {
    position: relative;
    font-family: "Roboto Condensed", Arial, sans-serif;
    color: var(--body);
    background: var(--white);
  }
  .abs { position: absolute; }

  /* Hero */
  .hero {
    position: absolute; left: 0; top: 0; width: 1200px; height: 733px;
    background:
      radial-gradient(ellipse 300px 280px at 560px 420px, rgba(230,200,170,0.35), rgba(0,0,0,0) 70%),
      linear-gradient(100deg, #1d2632 0%, #3a3f46 28%, #8a6a4a 52%, #d58a45 72%, #c25a1c 100%);
  }
  .brand { position: absolute; left: 97px; top: 40px; display: flex; flex-direction: column; align-items: center; gap: 14px; }
  .brand-mark { width: 70px; height: 70px; background: var(--orange); }
  .brand-name { color: #e6e6e6; font-size: 18px; letter-spacing: 6px; font-weight: 400; }
  .nav { position: absolute; top: 58px; right: 80px; display: flex; gap: 62px; }
  .nav a { color: var(--white); text-decoration: none; font-size: 24px; }
  .nav-active { position: absolute; left: 517px; top: 0; width: 95px; height: 5px; background: var(--white); }
  .hero-title { position: absolute; top: 228px; left: 0; width: 1200px; text-align: center; color: var(--white); font-size: 50px; font-weight: 400; }
  .hero-lead { position: absolute; top: 326px; left: 150px; width: 900px; text-align: center; color: var(--white); font-size: 25px; line-height: 37px; font-weight: 400; }
  .btn { position: absolute; left: 512px; top: 464px; width: 177px; height: 50px; background: var(--orange); color: var(--white); font-size: 22px; display: flex; align-items: center; justify-content: center; border-bottom: 3px solid var(--orange-dark); border-radius: 2px; }
  .dots { position: absolute; top: 690px; left: 548px; display: flex; gap: 21px; }
  .dot { width: 21px; height: 21px; border-radius: 50%; background: var(--white); }
  .dot.active { background: transparent; border: 3px solid var(--white); position: relative; }
  .dot.active::after { content: ""; position: absolute; left: 4px; top: 4px; width: 7px; height: 7px; border-radius: 50%; background: var(--white); }

  /* Intro */
  .intro-title { position: absolute; top: 780px; left: 0; width: 1200px; text-align: center; color: var(--orange); font-size: 41px; font-weight: 400; }
  .intro-rule { position: absolute; top: 838px; left: 568px; width: 73px; height: 3px; background: var(--ink); }
  .intro-text { position: absolute; top: 856px; left: 250px; width: 700px; text-align: center; color: var(--ink); font-size: 17px; line-height: 23px; }

  /* Audience */
  .audience { position: absolute; left: 0; top: 962px; width: 1200px; height: 1229px; background: var(--panel); border-top: 2px solid var(--rule); }
  .persona-photo { position: absolute; width: 240px; height: 270px; }
  .persona-title { position: absolute; color: var(--orange); font-size: 20px; font-weight: 400; }
  .persona-rule { position: absolute; height: 3px; width: 75px; background: var(--ink); }
  .persona-text { position: absolute; color: #2e2e2e; font-size: 15.5px; line-height: 23px; }

  /* Footer */
  .footer { position: absolute; left: 0; top: 2191px; width: 1200px; height: 317px; background: var(--footer); }
  .footer-base { position: absolute; left: 0; top: 2508px; width: 1200px; height: 42px; background: var(--footer-base); color: var(--white); font-size: 16px; display: flex; align-items: center; justify-content: center; }
  .footer-base b { color: var(--orange); font-weight: 700; }
  .col-title { position: absolute; top: 2206px; color: var(--orange); font-size: 31px; font-weight: 400; }
  .news-item { position: absolute; left: 80px; width: 298px; }
  .news-headline { color: var(--white); font-size: 16px; line-height: 21px; }
  .news-date { color: var(--muted); font-size: 13px; margin-top: 3px; }
  .news-sep { position: absolute; left: 80px; width: 298px; border-top: 1px dashed #8a8a8a; }
  .tweet { position: absolute; left: 442px; display: flex; gap: 12px; }
  .tweet-avatar { width: 56px; height: 56px; background: #2a2a2a; border: 2px solid #3a3a3a; display: flex; align-items: center; justify-content: center; }
  .tweet-avatar span { width: 30px; height: 30px; background: var(--orange); }
  .tweet-handle { color: var(--orange); font-size: 13px; line-height: 18px; }
  .tweet-text { color: var(--white); font-size: 14px; line-height: 19px; }
  .tweet-link { color: var(--muted); font-size: 13px; line-height: 18px; }
  .contact-label { position: absolute; left: 811px; color: var(--orange); font-size: 22px; }
  .contact-phone { position: absolute; left: 838px; color: var(--white); font-size: 16px; }
  .social { position: absolute; top: 2423px; width: 53px; height: 60px; }
</style>
</head>
<body>

<header class="hero" role="img" aria-label="Photo of a glass globe resting on a laptop keyboard, warm orange light">
</header>
<div class="nav-active"></div>
<div class="brand">
  <div class="brand-mark"></div>
  <div class="brand-name">VELTRA</div>
</div>
<nav class="nav">
  <a href="#">About</a>
  <a href="#">Services</a>
  <a href="#">Partners</a>
  <a href="#">Clients</a>
  <a href="#">Contact</a>
</nav>
<h1 class="hero-title">You need integration. We’re always there with you.</h1>
<p class="hero-lead">Veltra is one of the leading systems integrators to the world’s finance sector. We are an extension of your business and our services portfolio has been built so you always have access to a complete partner.</p>
<div class="btn">READ MORE</div>
<div class="dots"><span class="dot active"></span><span class="dot"></span><span class="dot"></span></div>

<h2 class="intro-title">Who Are You?</h2>
<div class="intro-rule"></div>
<p class="intro-text">If you’re part of a financial organisation, we have the power to help everyone work more efficiently, productively and profitably.</p>

<section class="audience"></section>

<!-- Persona 1 -->
<svg class="persona-photo" style="left:94px;top:1012px" viewBox="0 0 240 270" role="img" aria-label="Portrait photo of a smiling businessman in a grey suit">
  <defs><linearGradient id="g1" x1="0" y1="0" x2="0" y2="1"><stop offset="0" stop-color="#e4e4e4"/><stop offset="1" stop-color="#8a8d92"/></linearGradient></defs>
  <polygon points="120,1 239,68 239,202 120,269 1,202 1,68" fill="none" stroke="#f07421" stroke-width="1.5"/>
  <polygon points="120,10 231,73 231,197 120,260 9,197 9,73" fill="url(#g1)"/>
</svg>
<h3 class="persona-title" style="left:371px;top:1075px">Senior Hedge Fund Manager/CEO</h3>
<div class="persona-rule" style="left:371px;top:1109px"></div>
<p class="persona-text" style="left:371px;top:1124px;width:675px">You need to develop and implement strategies for business growth, while ensuring profitability. You’re aware your biggest asset is your staff and a happy workforce is a productive one. Security is a key concern in a changing always-on world and you need to be compliant, but you don’t want to overspend. Veltra can help you find the best solutions to help your business grow at the speed you want it to.</p>

<!-- Persona 2 -->
<h3 class="persona-title" style="left:80px;top:1326px">CFO</h3>
<div class="persona-rule" style="left:80px;top:1358px"></div>
<p class="persona-text" style="left:80px;top:1374px;width:660px">Your key responsibility is to obtain the maximum ROI from products and services. You understand investment opportunities, providing they return higher efficiencies and revenues. You are concerned more with long-term spending versus short-term and how you can get the most value out of a proposition. Veltra can advise how to boost ROI by streamlining your business to maximise return.</p>
<svg class="persona-photo" style="left:833px;top:1304px" viewBox="0 0 240 270" role="img" aria-label="Portrait photo of a smiling woman with long brown hair">
  <defs><linearGradient id="g2" x1="0" y1="0" x2="0" y2="1"><stop offset="0" stop-color="#e2e2e2"/><stop offset="1" stop-color="#9a8272"/></linearGradient></defs>
  <polygon points="120,1 239,68 239,202 120,269 1,202 1,68" fill="none" stroke="#f07421" stroke-width="1.5"/>
  <polygon points="120,10 231,73 231,197 120,260 9,197 9,73" fill="url(#g2)"/>
</svg>

<!-- Persona 3 -->
<svg class="persona-photo" style="left:94px;top:1573px" viewBox="0 0 240 270" role="img" aria-label="Portrait photo of a smiling young man in a dark suit">
  <defs><linearGradient id="g3" x1="0" y1="0" x2="0" y2="1"><stop offset="0" stop-color="#e6e6e6"/><stop offset="1" stop-color="#5d6066"/></linearGradient></defs>
  <polygon points="120,1 239,68 239,202 120,269 1,202 1,68" fill="none" stroke="#f07421" stroke-width="1.5"/>
  <polygon points="120,10 231,73 231,197 120,260 9,197 9,73" fill="url(#g3)"/>
</svg>
<h3 class="persona-title" style="left:371px;top:1639px">IT Manager/CTO</h3>
<div class="persona-rule" style="left:371px;top:1672px"></div>
<p class="persona-text" style="left:371px;top:1687px;width:690px">Integration with partners and services is your key concern. You want to make sure any IT system you implement will work with the whole infrastructure of your company. You don’t want your team to waste valuable time dealing with things that don’t matter. Veltra provides the whole picture to ensure your company is ready for the next generation of IT.</p>

<!-- Persona 4 -->
<h3 class="persona-title" style="left:80px;top:1889px">Employees</h3>
<div class="persona-rule" style="left:80px;top:1920px"></div>
<p class="persona-text" style="left:80px;top:1936px;width:670px">You’re working hard, but not getting anywhere fast. You want the tools to make your job easier so you can spend more time thinking about what you’re doing rather than how you’re doing it. You shouldn’t have to think about the technology you’re using, because it should just work. Veltra can help you get back on track everyday.</p>
<svg class="persona-photo" style="left:833px;top:1855px" viewBox="0 0 240 270" role="img" aria-label="Photo of office staff reviewing paperwork at a desk">
  <defs><linearGradient id="g4" x1="0" y1="0" x2="1" y2="1"><stop offset="0" stop-color="#f0f0f0"/><stop offset="0.6" stop-color="#9a8a7e"/><stop offset="1" stop-color="#3a3230"/></linearGradient></defs>
  <polygon points="120,1 239,68 239,202 120,269 1,202 1,68" fill="none" stroke="#f07421" stroke-width="1.5"/>
  <polygon points="120,10 231,73 231,197 120,260 9,197 9,73" fill="url(#g4)"/>
</svg>

<!-- Footer -->
<footer class="footer"></footer>
<h4 class="col-title" style="left:80px">Latest News</h4>
<h4 class="col-title" style="left:444px">Latest Tweets</h4>
<h4 class="col-title" style="left:811px">Contact Us</h4>

<div class="news-item" style="top:2262px"><div class="news-headline">Cloud growth in the financial sector</div><div class="news-date">Friday, 6 March 2015</div></div>
<div class="news-sep" style="top:2313px"></div>
<div class="news-item" style="top:2324px"><div class="news-headline">2015: Year of the cloud</div><div class="news-date">Friday, 27 February 2015</div></div>
<div class="news-sep" style="top:2375px"></div>
<div class="news-item" style="top:2386px"><div class="news-headline">Airlines reach new heights with the help of Cloud Computing</div><div class="news-date">Friday, 13 February 2015</div></div>

<div class="tweet" style="top:2261px">
  <div class="tweet-avatar"><span></span></div>
  <div><div class="tweet-handle">@Veltra_</div><div class="tweet-text">Dana Merrow spills the beans on Orchard Pay</div><div class="tweet-link">http://lnk.example/JGeXL</div></div>
</div>
<div class="tweet" style="top:2334px">
  <div class="tweet-avatar"><span></span></div>
  <div><div class="tweet-handle">@Veltra_</div><div class="tweet-text">How the Sorel Pictures attack changed</div><div class="tweet-link">http://lnk.example/JGeMJ</div></div>
</div>
<div class="tweet" style="top:2407px">
  <div class="tweet-avatar"><span></span></div>
  <div><div class="tweet-handle">@Veltra_</div><div class="tweet-text">Trust in the digital world: Is it at an all</div><div class="tweet-link">http://lnk.example/JGesQ</div></div>
</div>

<div class="contact-label" style="top:2258px">SUPPORT:</div>
<div class="contact-phone" style="top:2301px">+44 20 7946 0123</div>
<div class="contact-label" style="top:2342px">SALES:</div>
<div class="contact-phone" style="top:2385px">+44 20 7946 0124</div>

<svg class="social" style="left:821px" viewBox="0 0 53 60" role="img" aria-label="Social network link"><polygon points="26.5,0 53,15 53,45 26.5,60 0,45 0,15" fill="#f07421"/></svg>
<svg class="social" style="left:894px" viewBox="0 0 53 60" role="img" aria-label="Social network link"><polygon points="26.5,0 53,15 53,45 26.5,60 0,45 0,15" fill="#ffffff"/></svg>
<svg class="social" style="left:967px" viewBox="0 0 53 60" role="img" aria-label="Social network link"><polygon points="26.5,0 53,15 53,45 26.5,60 0,45 0,15" fill="#ffffff"/></svg>
<svg class="social" style="left:1039px" viewBox="0 0 53 60" role="img" aria-label="Social network link"><polygon points="26.5,0 53,15 53,45 26.5,60 0,45 0,15" fill="#ffffff"/></svg>

<div class="footer-base">©&nbsp;<b>Veltra</b>&nbsp;- 2015. All Rights Reserved.</div>

</body>
</html>
```